Namecard Designs+Logo for a High End Automobile Company

We need a new business card for our company called Velta Motorhof.

www.veltamotorhof.example.sg
Our new website will be up in 2.5 months time.

We sell used and brand new continental cars like Stavaro, KTJ, Lindqvar, Castrelli and etc. Currently we are operating from 2 offices in Singapore and United Kingdom.

We want a design which is serious. We are open to colours but try to keep it at a maximum of 3 colours.

We prefer something simple and minimal. We are open to 2 sides printing or even 2 sided namecards. Both UK and Singapore company offices address must be in; either side by side, front and back, or even 2 sided cards.

The logo can be a text logo, emblem, abstract, pictorial or combination.

We are printing with Prinvo.example so please kindly follow the printing guideline.

http://uk.prinvo.example/help/faq/templates-and-guidelines.html

Target Market(s)

Rich and Car Enthusiasts

Industry/Entity Type

Printing

Requirements
Must have
• Our 2 offices; UK and Singapore.

Our slogan which is " The Automobile Specialist"
Should not have
• Not more than 3 colours

```html
<!DOCTYPE html>
<html lang="en">
<head>
<meta charset="utf-8">
<title>Velta Motorhof — Logo and Business Card</title>
<link rel="stylesheet" href="https://fonts.googleapis.com/css2?family=Archivo+Black&family=Archivo:wght@700&family=Tinos:wght@400;700&display=swap">
<style>
  :root {
    --board: #3b3b3d;
    --brand-red: #e8232a;
    --deep-red: #a8151c;
    --paper: #ffffff;
    --rule: #c9c9c9;
    --soft-white: #fbe3e4;
  }
  * { margin: 0; padding: 0; box-sizing: border-box; }
  html, body { width: 1200px; height: 900px; overflow: hidden; }
  body { background: var(--board); position: relative; font-family: "Tinos", "Times New Roman", serif; }

  .board-title {
    position: absolute; left: 40px; top: 40px;
    font-family: "Archivo Black", Arial, sans-serif;
    font-size: 37px; color: var(--paper); letter-spacing: 0.5px; line-height: 1;
  }

  .logo-panel {
    position: absolute; left: 42px; top: 94px; width: 360px; height: 293px;
    background: var(--paper); border: 2px solid #d8d8d8;
  }

  .mark-dot { position: absolute; background: var(--brand-red); border-radius: 50%; }
  .wordmark {
    position: absolute; left: 0; width: 100%; text-align: center;
    font-family: "Archivo", Arial, sans-serif; font-weight: 700; color: var(--deep-red);
    white-space: nowrap; line-height: 1;
  }
  .wordmark-rule { position: absolute; height: 3px; background: var(--rule); }

  .card-back {
    position: absolute; left: 497px; top: 56px; width: 660px; height: 366px;
    background: var(--brand-red);
  }
  .card-back .mark-square {
    position: absolute; left: 300px; top: 60px; width: 60px; height: 60px; background: var(--paper);
  }
  .card-back .wordmark { top: 150px; font-size: 48px; color: var(--paper); }
  .slogan {
    position: absolute; left: 0; width: 100%; top: 214px; text-align: center;
    font-size: 22px; color: var(--soft-white); letter-spacing: 3px; text-transform: uppercase;
  }
  .brick-band {
    position: absolute; left: 40px; top: 294px; width: 580px; height: 58px;
    background: linear-gradient(90deg, rgba(255,255,255,0.45), rgba(255,255,255,0.7) 50%, rgba(255,255,255,0.35));
    border-radius: 4px;
  }

  .card-front {
    position: absolute; left: 192px; top: 464px; width: 674px; height: 370px;
    background: var(--brand-red);
  }
  .card-front .front-logo-side {
    position: absolute; left: 0; top: 0; width: 298px; height: 100%; background: var(--paper);
  }
  .holder-name {
    position: absolute; left: 298px; width: 376px; top: 20px; text-align: center;
    font-weight: 700; font-size: 30px; color: var(--paper);
  }
  .holder-role {
    position: absolute; left: 298px; width: 376px; top: 55px; text-align: center;
    font-size: 21px; color: var(--soft-white);
  }
  .contact-list { position: absolute; left: 336px; top: 168px; list-style: none; }
  .contact-list li {
    display: flex; align-items: center; height: 19.5px;
    font-size: 17.5px; color: var(--paper); line-height: 1; white-space: nowrap;
  }
  .contact-list svg { width: 18px; height: 16px; margin-right: 12px; flex: none; }
</style>
</head>
<body>

  <h1 class="board-title">LOGO DESIGNED</h1>

  <section class="logo-panel" aria-label="Logo">
    <div class="mark-dot" style="left:150px; top:50px; width:60px; height:60px;"></div>
    <div class="wordmark-rule" style="left:18px; right:18px; top:188px;"></div>
    <div class="wordmark" style="top:204px; font-size:36px;">Velta Motorhof</div>
    <div class="wordmark-rule" style="left:18px; right:18px; top:252px;"></div>
  </section>

  <section class="card-back" aria-label="Business card back">
    <div class="mark-square"></div>
    <div class="wordmark">Velta Motorhof</div>
    <div class="slogan">The Automobile Specialist</div>
    <div class="brick-band" role="img" aria-label="Staggered band of white rounded bars in varying opacity"></div>
  </section>

  <section class="card-front" aria-label="Business card front">
    <div class="front-logo-side">
      <div class="mark-dot" style="left:120px; top:98px; width:58px; height:58px;"></div>
      <div class="wordmark-rule" style="left:18px; right:18px; top:220px;"></div>
      <div class="wordmark" style="top:232px; font-size:32px;">Velta Motorhof</div>
      <div class="wordmark-rule" style="left:18px; right:18px; top:268px;"></div>
    </div>

    <div class="holder-name">Rowan Teale</div>
    <div class="holder-role">Principal</div>

    <ul class="contact-list">
      <li>
        <svg viewBox="0 0 18 16" fill="none" stroke="#fff" stroke-width="1.6"><path d="M2 8 L9 2 L16 8"/><path d="M4 7 V14 H14 V7"/></svg>
        UK: 00 Harwell Row
      </li>
      <li><svg viewBox="0 0 18 16"></svg>London EC1A 0AA</li>
      <li>
        <svg viewBox="0 0 18 16" fill="none" stroke="#fff" stroke-width="1.6"><path d="M2 8 L9 2 L16 8"/><path d="M4 7 V14 H14 V7"/></svg>
        SG: 00 Tembra Road
      </li>
      <li><svg viewBox="0 0 18 16"></svg>Singapore 000000</li>
      <li>
        <svg viewBox="0 0 18 16"><rect x="1" y="3" width="16" height="11" rx="1.5" fill="#fff"/><path d="M1.5 4 L9 9.5 L16.5 4" stroke="#e8232a" stroke-width="1.3" fill="none"/></svg>
        rowan@veltamotorhof.example.sg
      </li>
      <li>
        <svg viewBox="0 0 18 16" fill="none" stroke="#fff" stroke-width="1.5"><circle cx="9" cy="8" r="6.5"/><ellipse cx="9" cy="8" rx="2.8" ry="6.5"/><path d="M2.5 8 H15.5"/></svg>
        www.veltamotorhof.example.sg
      </li>
      <li>
        <svg viewBox="0 0 18 16" fill="#fff"><path d="M1 6 C4 1 14 1 17 6 L14 8 L12 5.5 H6 L4 8 Z"/><rect x="4" y="9" width="10" height="6" rx="1"/></svg>
        770-555-0184
      </li>
      <li>
        <svg viewBox="0 0 18 16" fill="#fff"><rect x="4" y="1" width="10" height="5"/><rect x="1" y="6" width="16" height="9" rx="1"/><rect x="4" y="9" width="10" height="2" fill="#e8232a"/></svg>
        770-555-0190
      </li>
      <li>
        <svg viewBox="0 0 18 16" fill="#fff"><rect x="5.5" y="0.5" width="7" height="15" rx="1.2"/><rect x="7" y="2.5" width="4" height="7" fill="#e8232a"/></svg>
        770-555-0164
      </li>
    </ul>
  </section>

</body>
</html>
```